Website Design for Gold Buying Company in Australia

We are looking for a Website layout for a company who buy gold pieces from trade and the public.

They would like to communicate that its easy, safe, a great way to make more money, and they pay the best prices in australia for Gold jewelery

Target Market(s)

Adults based in Australia aged 25-60 who are looking to make some extra money

Industry/Entity Type

It Company

Number of Pages Required

2 pages

Requirements
Must have
• Must have a homepage and a page to use for content.

• Will have a feed for the latest Gold, silver and platinum prices they are buying and selling at.

• Needs to have a from on the homepage where people can submit their details to be sent a ''Treasure Pouch'' which allows them to send gold pieces to eb valued and bought by the company.

Nice to have
• Would be nice to have a steped out graphic of how the ''Treasure Pouch by mail'' process works [Request a Kit, Send in your Gold, We Value and grade it, We pay you cash, cheque of Direct Deposit]

• Imagery will be gold related

• Colour schemes are not a major Issue-but using some gold or silver would be a good idea
Should not have
• No cheesy gold graphics please :)

```html
<!DOCTYPE html>
<html lang="en">
<head>
<meta charset="utf-8">
<title>Meridian Gold Buyers</title>
<link href="https://fonts.googleapis.com/css2?family=Arimo:wght@400;700&display=swap" rel="stylesheet">
<style>
:root{
  --gold:#f5b800;
  --panel:#454545;
  --band:#2f353d;
  --band-title:#3a4049;
  --ink:#ffffff;
  --muted:#dcdcdc;
  --field:#e6e6e6;
}
*{margin:0;padding:0;box-sizing:border-box}
html,body{width:1200px;height:1048px;overflow:hidden}
body{background:var(--gold);font-family:"Arimo",Arial,sans-serif;color:var(--ink);position:relative}
.site{position:absolute;left:84px;top:63px;width:1032px;height:921px;background:var(--panel);box-shadow:0 0 6px rgba(0,0,0,.35)}
.abs{position:absolute}
.gold-band{left:0;top:75px;width:1032px;height:33px;background:var(--gold)}
.brand{left:100px;top:22px;width:206px;height:206px;border-radius:50%;background:var(--band);border:4px solid var(--gold);display:flex;align-items:center;justify-content:center;text-align:center}
.brand-name{font-weight:700;font-size:24px;line-height:28px;color:var(--gold)}
.nav{left:420px;top:142px;width:581px;height:41px;border:2px solid #e9e9e9;border-radius:21px;display:flex;align-items:center;justify-content:center;gap:8px;font-size:13px;font-weight:700}
.nav a{color:var(--ink);text-decoration:none}
.nav a.current{color:var(--gold)}
.hero{left:427px;top:195px;width:574px;height:314px;border-radius:16px;overflow:hidden;background:radial-gradient(ellipse at 45% 40%,#d8c48e 0%,#9c8350 35%,#4b4335 70%,#2b2722 100%)}
.hero-bar{left:0;top:244px;width:100%;height:35px;background:rgba(120,120,120,.55)}
.slides{right:24px;top:253px;display:flex;gap:8px}
.slides span{width:18px;height:16px;background:#b9b9b9;color:#fff;font-size:10px;display:flex;align-items:center;justify-content:center}
.loading{left:28px;top:285px;font-size:10px;line-height:12px;color:#fff}
.loading b{font-weight:400;color:var(--gold);display:block;border-bottom:2px solid #fff;width:56px}
.welcome{left:33px;top:242px;width:380px}
.welcome h1{font-size:17px;color:var(--gold);font-weight:700;margin-bottom:6px}
.welcome p{font-size:12px;line-height:14px;color:var(--muted);margin-bottom:20px}
.process{left:32px;top:558px;width:1000px;height:174px;background:var(--band)}
.process-title{left:302px;top:8px;padding:4px 6px;background:var(--band-title);font-size:16px;font-weight:700;font-variant:small-caps;text-decoration:underline}
.step{top:50px;text-align:center;font-weight:700;font-variant:small-caps;font-size:15px;line-height:14px;color:#e8e8e8}
.step .icon{height:54px;display:flex;align-items:flex-end;justify-content:center;margin-bottom:12px}
.step-pay .icon{margin-bottom:4px}
.arrow{top:84px}
.request{left:48px;top:522px;width:272px;height:268px;border-radius:20px;border:6px solid #2a3038;background:linear-gradient(#343b44 0%,#343b44 74%,#7c838c 100%);text-align:center}
.request h2{margin-top:28px;font-size:19px;font-weight:700;font-variant:small-caps;color:var(--gold);white-space:nowrap}
.field{display:block;margin:16px auto 0;width:222px;height:34px;background:var(--field);color:#222;font-size:15px;line-height:34px}
.field + .field{margin-top:3px}
.submit{display:inline-block;margin-top:10px;width:102px;height:24px;border-radius:12px;background:var(--field);color:#1b2530;font-weight:700;font-size:16px;line-height:24px}
.request p{margin:12px auto 0;width:200px;font-size:13px;line-height:15px}
.process-note{left:336px;top:739px;width:652px;font-size:12px;line-height:14px;color:var(--muted)}
.footer-col h3{font-size:17px;font-weight:700;margin-bottom:6px}
.footer-links{font-size:12px;line-height:14px;color:var(--muted)}
.divider{left:499px;top:836px;width:2px;height:44px;background:#5d5d5d}
.footer-brand{left:870px;top:786px;width:92px;height:92px;border-radius:50%;background:#cfcfcf;border:3px solid #8a8a8a;display:flex;align-items:center;justify-content:center;text-align:center}
.footer-brand span{font-size:11px;font-weight:700;color:#333;line-height:13px}
.copyright{right:36px;top:883px;font-size:12px;color:var(--muted)}
</style>
</head>
<body>
<div class="site">
  <div class="abs gold-band"></div>
  <div class="abs brand"><span class="brand-name">Meridian<br>Gold Buyers</span></div>

  <nav class="abs nav">
    <a href="#">|home</a><a href="#">|about us</a><a href="#">|what we buy &amp; sell?</a><a href="#">|how it works</a><a href="#">|comments</a><a href="#">|bullion</a><a href="#" class="current">|trade inquiries</a>
  </nav>

  <div class="abs hero" role="img" aria-label="Photograph of gold jewellery, chains and pearl necklaces spilling from a dark jewellery box">
    <div class="abs hero-bar"></div>
    <div class="abs slides"><span>1</span><span>2</span><span>3</span><span>4</span></div>
    <div class="abs loading">98%<b>LOADING...</b></div>
  </div>

  <section class="abs welcome">
    <h1>Welcome to Meridian Gold Buyers</h1>
    <p>Lorem ipsum dolor sit amet, consetetur sadipscing elitr, sed diam nonumy eirmod tempor invidunt ut labore et dolore magna aliquyam erat, sed diam voluptua. Lorem ipsum dolor sit amet, consetetur sadipscing elitr, sed diam nonumy eirmod tempor invidunt ut labore et dolore magna aliquyam erat, sed diam voluptua.</p>
    <p>Lorem ipsum dolor sit amet, consetetur sadipscing elitr, sed diam nonumy eirmod tempor invidunt ut labore et dolore magna aliquyam erat, sed diam voluptua. Lorem ipsum dolor sit amet, consetetur sadipscing elitr, sed diam nonumy eirmod tempor invidunt ut labore et dolore magna aliquyam erat, sed diam voluptua.</p>
    <p>Lorem ipsum dolor sit amet, consetetur sadipscing elitr, sed diam nonumy eirmod tempor invidunt ut labore et dolore magna aliquyam erat, sed diam voluptua. .</p>
  </section>

  <section class="abs process">
    <div class="abs process-title">Treasure Pouch by Mail Process</div>

    <div class="abs step" style="left:309px;width:110px">
      <div class="icon"><svg width="40" height="42" viewBox="0 0 40 42"><path d="M0 0h40v30L28 42H0z" fill="var(--gold)"/><path d="M8 4l20 30" stroke="#2f353d" stroke-width="3"/></svg></div>
      Request a Kit
    </div>
    <svg class="abs arrow" style="left:427px" width="16" height="10" viewBox="0 0 16 10"><path d="M0 3h9V0l7 5-7 5V7H0z" fill="var(--gold)"/></svg>
    <div class="abs step" style="left:438px;width:146px">
      <div class="icon"><svg width="78" height="44" viewBox="0 0 78 44"><path d="M0 16h26M6 24h22M12 32h18" stroke="var(--gold)" stroke-width="3"/><path d="M34 10h40l4 34H30z" fill="var(--gold)"/><path d="M45 10V3h18v7" stroke="var(--gold)" stroke-width="3" fill="none"/></svg></div>
      Send in your Gold
    </div>
    <svg class="abs arrow" style="left:595px" width="16" height="10" viewBox="0 0 16 10"><path d="M0 3h9V0l7 5-7 5V7H0z" fill="var(--gold)"/></svg>
    <div class="abs step" style="left:607px;width:179px">
      <div class="icon"><svg width="52" height="46" viewBox="0 0 52 46"><rect x="2" y="4" width="12" height="42" fill="var(--gold)"/><rect x="18" y="20" width="12" height="26" fill="var(--gold)"/><rect x="34" y="30" width="12" height="16" fill="var(--gold)"/><text x="36" y="16" font-size="16" font-weight="700" fill="var(--gold)" font-family="Arimo,sans-serif">%</text></svg></div>
      We Value and grade it
    </div>
    <svg class="abs arrow" style="left:800px" width="16" height="10" viewBox="0 0 16 10"><path d="M0 3h9V0l7 5-7 5V7H0z" fill="var(--gold)"/></svg>
    <div class="abs step step-pay" style="left:818px;width:140px">
      <div class="icon"><svg width="58" height="44" viewBox="0 0 58 44"><rect x="0" y="14" width="58" height="14" fill="var(--gold)"/><circle cx="29" cy="21" r="16" fill="var(--gold)"/><text x="29" y="30" text-anchor="middle" font-size="24" font-weight="700" fill="#2f353d" font-family="Arimo,sans-serif">$</text></svg></div>
      We pay you cash,<br>cheque or<br>Direct Deposit
    </div>
  </section>

  <form class="abs request">
    <h2>Request a Treasure Pouch</h2>
    <span class="field">Type In Your Name</span>
    <span class="field">Type In Your Email</span>
    <span class="submit">SUBMIT</span>
    <p>Lorem ipsum dolor sit amet, consetetur sadipscing elitr, sed diam nonumy eirmod</p>
  </form>

  <p class="abs process-note">Lorem ipsum dolor sit amet, consetetur sadipscing elitr, sed diam nonumy eirmod tempor invidunt ut labore et dolore magna aliquyam erat, sed diam voluptua. Lorem ipsum dolor sit amet, consetetur sadipscing elitr, sed diam nonumy eirmod tempor invidunt ut labore et dolore magna aliquyam erat, sed diam voluptua.</p>

  <div class="abs footer-col" style="left:361px;top:810px">
    <h3>Meridian Gold Buyers</h3>
    <div class="footer-links">About Us<br>What We Buy &amp; Sell?<br>Privacy Policy</div>
  </div>
  <div class="abs divider"></div>
  <div class="abs footer-links" style="left:516px;top:834px">Trade Inquiries<br>Contact</div>
  <div class="abs footer-col" style="left:597px;top:810px">
    <h3>Help &amp; Info</h3>
    <div class="footer-links" style="margin-left:22px">How it Works<br>Comments<br>Bullion</div>
  </div>

  <div class="abs footer-brand"><span>Meridian<br>Gold Buyers</span></div>
  <div class="abs copyright">© 2009 meridiangold.com.au</div>
</div>
</body>
</html>
```